Business Card for Ferncliff Massage

I need a business card for my massage therapy & cannabis oil practice. I already have a logo,the "massage" got edited out of this file. I will send the original soon. I need these elements to be on the card:
web: FerncliffMassage.example
ph: 417/283-9061
email: Mirela.Dawkant@mailbox.example
Other slogans, statements to consider:
Science Geek, Massage Therapist, Neuromuscular Therapy, Cannabis Spa Treatments, Raindrop Therapy, Essential Oils
Target Market(s)
women between 20 & 65, people with enough $ to afford regular massage, people who recently had a motor vehicle accident, Halvora HMP insured
Industry/Entity Type
Massage Therapy
Contact Information for Business Card
I would like to see my bear logo featured; contact details, greens & blues preferred colors.

```html
<!DOCTYPE html>
<html lang="en">
<head>
<meta charset="utf-8">
<title>Ferncliff Massage – Business Card</title>
<link href="https://fonts.googleapis.com/css2?family=Open+Sans:wght@400;600;700&display=swap" rel="stylesheet">
<style>
  :root {
    --page-bg: #e4e6e8;
    --brand-blue: #0a7bbf;
    --brand-teal: #00a98f;
    --frost: #f1f3f4;
    --ink-white: #ffffff;
    --faint-blue: #a9cde3;
  }
  * { margin: 0; padding: 0; box-sizing: border-box; }
  html, body {
    width: 1200px; height: 900px; overflow: hidden;
    background: var(--page-bg);
    font-family: "Open Sans", Arial, sans-serif;
  }
  .canvas { position: relative; width: 1200px; height: 900px; }
  .card {
    position: absolute; display: flex;
    box-shadow: 0 6px 18px rgba(0,0,0,0.12);
  }
  .card--front { left: 238px; top: 62px; width: 555px; height: 343px; }
  .card--back  { left: 458px; top: 518px; width: 559px; height: 344px; }

  .panel { height: 100%; position: relative; }
  .panel--contact { width: 277px; background: var(--brand-blue); color: var(--ink-white); }
  .panel--brand { flex: 1; background: var(--frost); }
  .panel--ghost { width: 274px; background: var(--frost); }
  .panel--services { flex: 1; background: var(--brand-teal); color: var(--ink-white); }

  .person { position: absolute; left: 24px; top: 86px; }
  .person__name { font-size: 18px; font-weight: 700; line-height: 24px; }
  .person__role { font-size: 15px; font-weight: 400; line-height: 22px; }

  .contact-list { position: absolute; left: 24px; top: 193px; list-style: none; }
  .contact-list li {
    display: flex; align-items: center; gap: 8px;
    font-size: 14px; line-height: 20.5px;
  }
  .contact-list svg { width: 12px; height: 12px; flex: none; fill: var(--ink-white); }

  .brand-mark {
    position: absolute; left: 0; right: 0; top: 88px;
    display: flex; flex-direction: column; align-items: center; gap: 22px;
  }
  .brand-mark__dot { width: 70px; height: 70px; border-radius: 50%; background: var(--brand-blue); }
  .brand-mark__name { font-size: 30px; font-weight: 400; color: var(--brand-teal); white-space: nowrap; }

  .ghost-mark {
    position: absolute; left: 0; right: 0; top: 200px; text-align: center;
    font-size: 30px; font-weight: 400; color: var(--faint-blue); white-space: nowrap;
  }

  .service-list { position: absolute; left: 32px; top: 93px; list-style: none; }
  .service-list li {
    position: relative; padding-left: 16px;
    font-size: 15px; line-height: 27.2px;
  }
  .service-list li::before {
    content: ""; position: absolute; left: 0; top: 10px;
    width: 7px; height: 7px; border-radius: 50%; background: var(--ink-white);
  }
</style>
</head>
<body>
<main class="canvas">
  <section class="card card--front">
    <div class="panel panel--contact">
      <div class="person">
        <p class="person__name">Daniel Harrow</p>
        <p class="person__role">Managing Director</p>
      </div>
      <ul class="contact-list">
        <li>
          <svg viewBox="0 0 12 12" aria-hidden="true"><path d="M1 4c0-2 2-3 5-3s5 1 5 3v1H8.5V3.8H3.5V5H1zM2.5 6h7l1 5h-9z"/></svg>
          417/283-9061
        </li>
        <li>
          <svg viewBox="0 0 12 12" aria-hidden="true"><path d="M0.5 2.5h11v7h-11z M1.2 3.2 6 6.6l4.8-3.4"/><path d="M1 3.3 6 7l5-3.7" fill="none" stroke="#0a7bbf" stroke-width="1"/></svg>
          Mirela.Dawkant@mailbox.example
        </li>
        <li>
          <svg viewBox="0 0 12 12" aria-hidden="true"><path d="M5 7 7 5M4.2 5.6 2.6 7.2a1.7 1.7 0 0 0 2.4 2.4l1.6-1.6M7.8 6.4l1.6-1.6A1.7 1.7 0 0 0 7 2.4L5.4 4" fill="none" stroke="#fff" stroke-width="1.3" stroke-linecap="round"/></svg>
          www.FerncliffMassage.example
        </li>
      </ul>
    </div>
    <div class="panel panel--brand">
      <div class="brand-mark">
        <span class="brand-mark__dot" aria-hidden="true"></span>
        <span class="brand-mark__name">Ferncliff Massage</span>
      </div>
    </div>
  </section>

  <section class="card card--back">
    <div class="panel panel--ghost">
      <span class="ghost-mark">Ferncliff Massage</span>
    </div>
    <div class="panel panel--services">
      <ul class="service-list">
        <li>Science Geek</li>
        <li>Massage Therapist</li>
        <li>Neuromuscular Therapy</li>
        <li>Cannabis Spa Treatments</li>
        <li>Raindrop Therapy</li>
        <li>Essential Oils</li>
      </ul>
    </div>
  </section>
</main>
</body>
</html>
```